Willow Glow & Laser - Business Banner with Brand Elements

Design:
• We would like to get a creative design for a wide banner that will go outside our medical spa clinic location. We need a designer to make a simple yet colorful and high-quality design layout. We want this banner to be eye-catching and to communicate the services we offer at our business: Laser Hair Removal | Velonix | Lip Filler.

Requirements:
• We would like the banner to include our companies information which is the following:

Logo
“Refresh Your Skin”
Laser Hair Removal | Velonix | Lip Filler
(555) 287-1936
www.WillowGlowLaser.com

Colors:
• Our business colors are orange, a hint of black and white, but mostly peach/orange tones. (Orange: #f78f20 , White: #ffffff)

Fonts:
• Josefins Sans Bold & Lato

Content and images can be located here:
https://files.cloudvaultshare.com/folders/7tQmZ2xVbR9kLpN4sW8yH3cD6fJ1gA0eU?usp=sharing

The following will give you an idea of our brand presentation:
• Our website is: www.WillowGlowLaser.com
• Our Instagram; @willowglowlaser
• Our Facebook: www.socialpagehub.com/willowglowlaser

Target Market(s)
• Women 25 - 45

Industry/Entity Type
• Beauty

```html
<!DOCTYPE html>
<html lang="en">
<head>
<meta charset="utf-8">
<title>Willow Glow &amp; Laser – Banner Concepts</title>
<link href="https://fonts.googleapis.com/css2?family=Josefin+Sans:wght@700&family=Lato:wght@400;700&display=swap" rel="stylesheet">
<style>
  :root{
    --orange:#f78f20;
    --ink:#111111;
    --white:#ffffff;
    --board:#636363;
    --sand:#d9c3a5;
    --sky:#8fcfe0;
    --sea:#3fb6c8;
  }
  *{margin:0;padding:0;box-sizing:border-box}
  html,body{width:1200px;height:583px;overflow:hidden;background:var(--board)}
  .board{position:relative;width:1200px;height:583px}
  .banner{position:absolute;width:544px;height:224px;background:var(--white);overflow:hidden}
  .banner--a{left:46px;top:40px}
  .banner--b{left:615px;top:40px}
  .banner--c{left:46px;top:303px}
  .banner--d{left:615px;top:303px}
  .banner svg.art{position:absolute;inset:0;width:544px;height:224px}
  .copy{position:absolute}
  .brand{display:flex;align-items:center;gap:5px;font-family:"Josefin Sans",sans-serif;font-weight:700;font-size:12.5px;color:var(--ink);white-space:nowrap}
  .brand-dot{width:22px;height:22px;border-radius:50%;background:var(--orange);flex:none}
  .headline{font-family:"Josefin Sans",sans-serif;font-weight:700;font-size:19px;color:var(--ink);margin-top:16px;white-space:nowrap;line-height:1}
  .headline--caps{text-transform:uppercase;font-size:18.5px;letter-spacing:.3px}
  .services{list-style:none;margin-top:13px}
  .services li{display:flex;align-items:center;gap:7px;font-family:"Lato",sans-serif;font-weight:700;font-size:9px;color:var(--orange);text-transform:uppercase;letter-spacing:.5px;height:21px}
  .bullet{width:8px;height:8px;border-radius:50%;background:var(--orange);flex:none}
  .service-line{display:flex;align-items:center;gap:4px;margin-top:10px;font-family:"Lato",sans-serif;font-weight:700;font-size:8px;color:var(--orange);letter-spacing:.4px;text-transform:uppercase;white-space:nowrap}
  .contact{font-family:"Lato",sans-serif;font-size:9px;color:var(--ink);line-height:17px;margin-top:6px}
  .contact--icons{margin-top:12px}
  .contact--icons p{display:flex;align-items:center;gap:8px;height:19px;font-weight:700;font-size:8.5px}
  .icon{width:10px;height:10px;flex:none}
</style>
</head>
<body>
<main class="board">

  <!-- Concept A -->
  <section class="banner banner--a">
    <svg class="art" viewBox="0 0 544 224">
      <defs>
        <linearGradient id="photoA" x1="0" y1="0" x2="1" y2="1">
          <stop offset="0" stop-color="#d8c2a4"/>
          <stop offset=".5" stop-color="#b98f72"/>
          <stop offset="1" stop-color="#e9dfd3"/>
        </linearGradient>
      </defs>
      <polygon points="228,0 544,0 544,224 302,224 202,70" fill="url(#photoA)" role="img" aria-label="Photo of three women with glowing skin posed together"/>
      <polygon points="202,70 302,224 294,224 196,80" fill="var(--orange)"/>
    </svg>
    <div class="copy" style="left:19px;top:18px">
      <div class="brand"><span class="brand-dot"></span>Willow Glow &amp; Laser</div>
      <h1 class="headline">Refresh Your Skin</h1>
      <ul class="services">
        <li><span class="bullet"></span>Laser Hair Removal</li>
        <li><span class="bullet"></span>Velonix</li>
        <li><span class="bullet"></span>Lip Filler</li>
      </ul>
      <div class="contact">
        <p>Phone: (555) 287-1936</p>
        <p>www.WillowGlowLaser.com</p>
      </div>
    </div>
  </section>

  <!-- Concept B -->
  <section class="banner banner--b">
    <svg class="art" viewBox="0 0 544 224">
      <defs>
        <linearGradient id="photoB" x1="0" y1="0" x2="0" y2="1">
          <stop offset="0" stop-color="#9fd6e6"/>
          <stop offset=".45" stop-color="#cfe9ee"/>
          <stop offset=".7" stop-color="#e8e2d6"/>
          <stop offset="1" stop-color="#e3d2bb"/>
        </linearGradient>
      </defs>
      <path d="M200,0 L544,0 L544,224 L300,224 L290,205 L285,186 L272,170 L266,150 L254,134 L246,112 L240,96 L232,78 L236,62 L224,48 L228,34 L214,22 L210,10 Z" fill="url(#photoB)" role="img" aria-label="Photo of a smiling woman in a striped swimsuit on a breezy beach"/>
    </svg>
    <div class="copy" style="left:28px;top:41px">
      <div class="brand"><span class="brand-dot"></span>Willow Glow &amp; Laser</div>
      <h2 class="headline headline--caps">Refresh Your Skin</h2>
      <p class="service-line"><span class="bullet"></span>Laser Hair Removal | Velonix | Lip Filler</p>
      <div class="contact contact--icons">
        <p><svg class="icon" viewBox="0 0 10 10"><circle cx="5" cy="5" r="5" fill="var(--orange)"/><path d="M3.2 2.6 L4.2 3.8 L3.8 4.4 Q4.6 5.8 5.6 6.2 L6.2 5.8 L7.4 6.8 L6.6 7.6 Q4 7.2 2.4 3.4 Z" fill="var(--white)"/></svg>Phone: (555) 287-1936</p>
        <p><svg class="icon" viewBox="0 0 10 10"><circle cx="5" cy="5" r="4.4" fill="none" stroke="var(--orange)" stroke-width="1.1"/><ellipse cx="5" cy="5" rx="1.8" ry="4.4" fill="none" stroke="var(--orange)" stroke-width=".9"/><line x1=".6" y1="5" x2="9.4" y2="5" stroke="var(--orange)" stroke-width=".9"/></svg>www.WillowGlowLaser.com</p>
      </div>
    </div>
  </section>

  <!-- Concept C -->
  <section class="banner banner--c">
    <svg class="art" viewBox="0 0 544 224">
      <defs>
        <linearGradient id="photoC" x1="0" y1="0" x2="0" y2="1">
          <stop offset="0" stop-color="#c9e2f2"/>
          <stop offset=".25" stop-color="#4cc3d3"/>
          <stop offset=".55" stop-color="#9fdde0"/>
          <stop offset=".8" stop-color="#e8dac6"/>
          <stop offset="1" stop-color="#e9ddcc"/>
        </linearGradient>
      </defs>
      <path d="M352,0 Q222,56 208,224 L544,224 L544,0 Z" fill="url(#photoC)" role="img" aria-label="Photo of a smiling woman lying on the sand at the edge of a turquoise sea"/>
      <path d="M348,0 Q210,58 196,224" fill="none" stroke="var(--orange)" stroke-width="4"/>
      <path d="M544,170 Q520,212 470,224" fill="none" stroke="var(--orange)" stroke-width="4"/>
    </svg>
    <div class="copy" style="left:22px;top:39px">
      <div class="brand"><span class="brand-dot"></span>Willow Glow &amp; Laser</div>
      <h2 class="headline headline--caps">Refresh Your Skin</h2>
      <p class="service-line"><span class="bullet"></span>Laser Hair Removal | Velonix | Lip Filler</p>
      <div class="contact contact--icons">
        <p><svg class="icon" viewBox="0 0 10 10"><circle cx="5" cy="5" r="5" fill="var(--orange)"/><path d="M3.2 2.6 L4.2 3.8 L3.8 4.4 Q4.6 5.8 5.6 6.2 L6.2 5.8 L7.4 6.8 L6.6 7.6 Q4 7.2 2.4 3.4 Z" fill="var(--white)"/></svg>Phone: (555) 287-1936</p>
        <p><svg class="icon" viewBox="0 0 10 10"><circle cx="5" cy="5" r="4.4" fill="none" stroke="var(--orange)" stroke-width="1.1"/><ellipse cx="5" cy="5" rx="1.8" ry="4.4" fill="none" stroke="var(--orange)" stroke-width=".9"/><line x1=".6" y1="5" x2="9.4" y2="5" stroke="var(--orange)" stroke-width=".9"/></svg>www.WillowGlowLaser.com</p>
      </div>
    </div>
  </section>

  <!-- Concept D -->
  <section class="banner banner--d">
    <svg class="art" viewBox="0 0 544 224">
      <defs>
        <linearGradient id="photoD" x1="0" y1="0" x2="0" y2="1">
          <stop offset="0" stop-color="#5fb7d4"/>
          <stop offset=".45" stop-color="#a8d9e3"/>
          <stop offset=".75" stop-color="#e6e6e0"/>
          <stop offset="1" stop-color="#efe7da"/>
        </linearGradient>
      </defs>
      <polygon points="0,0 235,0 347,224 0,224" fill="url(#photoD)" role="img" aria-label="Photo of a smiling woman in a straw sun hat on the beach"/>
      <polygon points="240,0 329,0 269,58" fill="var(--orange)"/>
    </svg>
    <div class="copy" style="left:357px;top:20px">
      <div class="brand"><span class="brand-dot"></span>Willow Glow &amp; Laser</div>
      <h2 class="headline">Refresh Your Skin</h2>
      <ul class="services">
        <li><span class="bullet"></span>Laser Hair Removal</li>
        <li><span class="bullet"></span>Velonix</li>
        <li><span class="bullet"></span>Lip Filler</li>
      </ul>
      <div class="contact">
        <p>Phone: (555) 287-1936</p>
        <p>www.WillowGlowLaser.com</p>
      </div>
    </div>
  </section>

</main>
</body>
</html>
```